Brindlewick Pest Control Hotel Brochure

Hi we are looking to get a slick looking brochure designed. It should be 8.5x11, open up to 17x11 and be a total of 4 pages. We are hoping that you guys have something pre-made and ready to go with a quick turn around.
Our target for this one is hotels. The front page should have a hotel of some sort on the front. Inside should say things like "You have pest problems, Brindlewick Pest Control has answers" Maybe some information and statistics that apply to the hotel industry regarding pest control in California/United States.
I have a high resolution logo of ours that I can send over when appropriate.
Our website is www.getbrindlewick.com if you want to see how our company design is.
Hotels

```html
<!DOCTYPE html>
<html lang="en">
<head>
<meta charset="utf-8">
<title>Brindlewick Pest Control – Hotel Brochure Spread</title>
<link href="https://fonts.googleapis.com/css2?family=Montserrat:ital,wght@0,400;0,600;0,700;0,800;1,400;1,700;1,800&display=swap" rel="stylesheet">
<style>
:root{
  --green:#6cbd45;
  --blue:#1a6fb9;
  --blue-dark:#125a9c;
  --ink:#3c3c3c;
  --muted:#5b5b5b;
  --paper:#f7f7f7;
  --bg:#e9eaec;
}
*{box-sizing:border-box;margin:0;padding:0}
html,body{width:1200px;height:833px;overflow:hidden;background:var(--bg);font-family:'Montserrat',sans-serif;color:var(--ink)}
.spread{position:absolute;left:30px;top:47px;width:1140px;height:738px;display:flex;box-shadow:0 6px 24px rgba(0,0,0,.18)}
.page{position:relative;width:570px;height:738px;background:var(--paper);overflow:hidden}
.page--left{border-right:1px solid #dcdcdc}
.page::after{content:"";position:absolute;left:0;right:0;bottom:0;height:4px;background:var(--green)}
.headline{position:absolute;color:var(--green);font-weight:800;font-size:36px;letter-spacing:.5px;white-space:nowrap}
.band{position:absolute;background:var(--blue);color:#fff;font-weight:800;white-space:nowrap;display:flex;align-items:center}
.band--sub{left:30px;top:92px;width:510px;height:38px;font-style:italic;font-size:21px;padding-left:24px;letter-spacing:.5px}
.band--title{left:30px;top:90px;width:520px;height:46px;font-size:32px;justify-content:center;letter-spacing:1px}
.photo{position:absolute}
.collage .photo--main{left:40px;top:150px;width:296px;height:232px;background:linear-gradient(120deg,#e6e1dc 0%,#d2cbc4 40%,#4a403c 70%,#e9e9ea 100%)}
.collage .photo--top{left:344px;top:150px;width:186px;height:112px;background:linear-gradient(120deg,#5b4a44,#e9e9e9 60%,#8a7c74)}
.collage .photo--bottom{left:344px;top:270px;width:186px;height:112px;background:linear-gradient(140deg,#cfc8c1,#ecebea 50%,#b7a99f)}
.rule{position:absolute;left:30px;right:30px;height:1.5px;background:var(--blue)}
.tab{position:absolute;background:var(--blue);color:#fff;font-weight:800;font-size:18px;letter-spacing:1.5px;height:34px;display:flex;align-items:center;justify-content:center}
.steps{position:absolute;left:30px;right:30px;top:448px;display:flex;justify-content:space-between}
.step{width:160px;text-align:center}
.step__icon{width:86px;height:86px;margin:0 auto 12px;border:2px solid var(--green);border-radius:50%;display:flex;align-items:center;justify-content:center;background:#fff}
.step__title{color:var(--blue);font-weight:800;font-size:15px;letter-spacing:1px;padding-bottom:5px;border-bottom:1.5px solid var(--green);margin:0 10px 8px}
.step__text{font-size:10px;line-height:1.45;color:var(--muted);font-style:italic}
.protect{position:absolute;left:30px;top:150px;width:510px;height:240px;display:flex}
.protect .photo--worker{position:relative;width:190px;height:100%;background:linear-gradient(90deg,#4e3d37,#7e6b62 60%,#d9d6d3)}
.pest-grid{flex:1;background:linear-gradient(135deg,#e7e7e7,#f1f1f1 50%,#dcdcdc);display:grid;grid-template-columns:repeat(3,1fr);grid-template-rows:repeat(3,1fr);padding:10px 6px}
.pest{display:flex;flex-direction:column;align-items:center;justify-content:center;gap:3px}
.pest__name{font-size:8.5px;font-weight:700;letter-spacing:.8px;color:#333;text-transform:uppercase}
.reasons{position:absolute;left:30px;right:30px;top:442px;display:flex;justify-content:space-between}
.reason{text-align:center}
.reason--elite{width:180px}
.reason--prices{width:158px}
.reason--variety{width:164px}
.reason__icon{height:40px;display:flex;justify-content:center;margin-bottom:4px}
.reason__title{color:var(--blue);font-weight:800;font-style:italic;font-size:12.5px;margin-bottom:5px}
.reason__text{font-size:9.5px;line-height:1.35;color:var(--muted);font-style:italic}
.cta{position:absolute;left:30px;right:30px;top:614px}
.cta__lead{margin-left:110px;width:300px;background:#fff;border:1.5px solid var(--blue);color:#333;font-weight:800;font-size:12.5px;letter-spacing:.8px;text-align:center;padding:4px 0 3px}
.cta__main{margin-left:110px;width:300px;background:var(--blue);color:#fff;font-weight:800;font-size:30px;letter-spacing:1px;text-align:center;line-height:38px;position:relative;z-index:1}
.cta__offer{margin-top:-12px;background:var(--green);color:#fff;border-radius:16px;padding:16px 20px 9px;text-align:center}
.cta__offer-line{font-size:16px;font-style:italic;line-height:1.25}
.cta__offer-strong{font-size:17px;font-weight:800;font-style:italic;letter-spacing:1px;line-height:1.25}
</style>
</head>
<body>
<main class="spread">

  <section class="page page--left">
    <h1 class="headline" style="left:40px;top:36px">You have pest problems,</h1>
    <div class="band band--sub">Brindlewick Pest Control has answers</div>

    <div class="collage">
      <div class="photo photo--main" role="img" aria-label="Technician in protective suit fogging a hotel bedroom"></div>
      <div class="photo photo--top" role="img" aria-label="Technician spraying along a wall"></div>
      <div class="photo photo--bottom" role="img" aria-label="Technician in respirator disinfecting a lounge"></div>
    </div>

    <div class="rule" style="top:415px"></div>
    <div class="tab" style="left:185px;top:399px;width:200px">WORK PRINCIPLE</div>

    <div class="steps">
      <article class="step">
        <div class="step__icon">
          <svg width="52" height="52" viewBox="0 0 52 52" fill="none" stroke="#888" stroke-width="1.6">
            <rect x="10" y="6" width="32" height="40" rx="2"/>
            <path d="M15 16l2 2 4-4M15 25l2 2 4-4M15 34l2 2 4-4" stroke="var(--green)"/>
            <path d="M25 17h12M25 26h12M25 35h12"/>
          </svg>
        </div>
        <h2 class="step__title">INSPECTION</h2>
        <p class="step__text">Our technicians will do a thorough inspection of the area to locate where your pests are hiding and seeking shelter.</p>
      </article>
      <article class="step">
        <div class="step__icon">
          <svg width="52" height="52" viewBox="0 0 52 52" fill="none" stroke="#888" stroke-width="1.6">
            <rect x="18" y="20" width="16" height="24" rx="3"/>
            <path d="M22 20v-6h8v6M30 14h10v8"/>
            <path d="M38 22v6" stroke="var(--green)" stroke-width="3"/>
          </svg>
        </div>
        <h2 class="step__title">DISINFECTION</h2>
        <p class="step__text">We spray the affected area using the latest chemical and treatment solution so bugs and insects are killed instantly.</p>
      </article>
      <article class="step">
        <div class="step__icon">
          <svg width="52" height="52" viewBox="0 0 52 52" fill="none" stroke="#888" stroke-width="1.6">
            <path d="M8 26L26 12l18 14M13 23v20h26V23"/>
            <path d="M22 43V32h8v11"/>
            <path d="M34 6v8M30 10h8M16 10v6M13 13h6" stroke="var(--green)"/>
          </svg>
        </div>
        <h2 class="step__title">PREVENTION</h2>
        <p class="step__text">Schedule a monthly, bi monthly, quarterly or yearly service with us to ensure pests are gone for good.</p>
      </article>
    </div>
  </section>

  <section class="page page--right">
    <h1 class="headline" style="left:70px;top:36px">How Can We Protect</h1>
    <div class="band band--title">Your Hotel?</div>

    <div class="protect">
      <div class="photo photo--worker" role="img" aria-label="Pest control technician in overalls holding a sprayer"></div>
      <div class="pest-grid">
        <div class="pest"><svg width="34" height="34" viewBox="0 0 34 34"><circle cx="17" cy="17" r="14" fill="#c98a5a" stroke="var(--blue)" stroke-width="3"/><path d="M7 27L27 7" stroke="var(--blue)" stroke-width="3"/></svg><span class="pest__name">Cockroaches</span></div>
        <div class="pest"><svg width="34" height="34" viewBox="0 0 34 34"><circle cx="17" cy="17" r="14" fill="#b8652c" stroke="var(--blue)" stroke-width="3"/><path d="M7 27L27 7" stroke="var(--blue)" stroke-width="3"/></svg><span class="pest__name">Fleas</span></div>
        <div class="pest"><svg width="34" height="34" viewBox="0 0 34 34"><circle cx="17" cy="17" r="14" fill="#a55a2e" stroke="var(--blue)" stroke-width="3"/><path d="M7 27L27 7" stroke="var(--blue)" stroke-width="3"/></svg><span class="pest__name">Ants</span></div>
        <div class="pest"><svg width="34" height="34" viewBox="0 0 34 34"><circle cx="17" cy="17" r="14" fill="#9a9a9a" stroke="var(--blue)" stroke-width="3"/><path d="M7 27L27 7" stroke="var(--blue)" stroke-width="3"/></svg><span class="pest__name">Mosquitoes</span></div>
        <div class="pest"><svg width="34" height="34" viewBox="0 0 34 34"><circle cx="17" cy="17" r="14" fill="#c99a3a" stroke="var(--blue)" stroke-width="3"/><path d="M7 27L27 7" stroke="var(--blue)" stroke-width="3"/></svg><span class="pest__name">Wasps</span></div>
        <div class="pest"><svg width="34" height="34" viewBox="0 0 34 34"><circle cx="17" cy="17" r="14" fill="#4a3a32" stroke="var(--blue)" stroke-width="3"/><path d="M7 27L27 7" stroke="var(--blue)" stroke-width="3"/></svg><span class="pest__name">Spiders</span></div>
        <div class="pest"><svg width="34" height="34" viewBox="0 0 34 34"><circle cx="17" cy="17" r="14" fill="#a7a19b" stroke="var(--blue)" stroke-width="3"/><path d="M7 27L27 7" stroke="var(--blue)" stroke-width="3"/></svg><span class="pest__name">Rodents</span></div>
        <div class="pest"><svg width="34" height="34" viewBox="0 0 34 34"><circle cx="17" cy="17" r="14" fill="#c0612e" stroke="var(--blue)" stroke-width="3"/><path d="M7 27L27 7" stroke="var(--blue)" stroke-width="3"/></svg><span class="pest__name">Bed Bugs</span></div>
        <div class="pest"><svg width="34" height="34" viewBox="0 0 34 34"><circle cx="17" cy="17" r="14" fill="#b2383a" stroke="var(--blue)" stroke-width="3"/><path d="M7 27L27 7" stroke="var(--blue)" stroke-width="3"/></svg><span class="pest__name">Covid-19</span></div>
      </div>
    </div>

    <div class="rule" style="top:415px"></div>
    <div class="tab" style="left:170px;top:399px;width:230px">WHY CHOOSE US</div>

    <div class="reasons">
      <article class="reason reason--elite">
        <div class="reason__icon"><svg width="56" height="40" viewBox="0 0 56 40" fill="none" stroke="var(--green)" stroke-width="1.6"><rect x="2" y="4" width="52" height="30" rx="2"/><circle cx="16" cy="17" r="7"/><path d="M12 24l-2 10 6-3 6 3-2-10M28 14h20M28 20h20M28 26h14"/></svg></div>
        <h2 class="reason__title">Elite Technicians</h2>
        <p class="reason__text">Our technicians are highly trained and qualified to recognize a variety of pests invading your commercial or residential property. They are up to date with the latest technology and available products so you can rest assure you receive the best treatment.</p>
      </article>
      <article class="reason reason--prices">
        <div class="reason__icon"><svg width="48" height="40" viewBox="0 0 48 40" fill="none" stroke="var(--green)" stroke-width="1.6"><path d="M4 18h8v18H4zM12 20l8-14c3 0 4 2 3 6l-1 5h10c3 0 4 3 2 5"/><rect x="26" y="16" width="18" height="22" rx="2"/><path d="M38 22c-2-2-6-1-6 1s6 2 6 5-4 3-6 1M35 20v2M35 30v2"/></svg></div>
        <h2 class="reason__title">Great Prices</h2>
        <p class="reason__text">When it comes to getting rid of those unwanted critters, our prices are unbeatable. Our rates are competitive so you can be at ease knowing our prices will fit into your range.</p>
      </article>
      <article class="reason reason--variety">
        <div class="reason__icon"><svg width="44" height="40" viewBox="0 0 44 40" fill="none" stroke="var(--green)" stroke-width="1.6"><circle cx="10" cy="10" r="5"/><circle cx="22" cy="6" r="5"/><circle cx="34" cy="10" r="5"/><path d="M10 15v6M22 11v6M34 15v6M10 21h24"/><path d="M18 38V26c0-2 4-2 4 0v4l8 2v6"/></svg></div>
        <h2 class="reason__title">Variety of Services</h2>
        <p class="reason__text">From the smallest animal like a termite to a slithering snake, we offer many different services so you can consider your one stop shop when it comes to termite and pest control.</p>
      </article>
    </div>

    <div class="cta">
      <div class="cta__lead">CONTACT US TODAY FOR YOUR</div>
      <div class="cta__main">FREE ESTIMATE</div>
      <div class="cta__offer">
        <p class="cta__offer-line">And get $50 off your initial visit. We also offer a</p>
        <p class="cta__offer-strong">100% MONEY BACK GUARANTEE</p>
      </div>
    </div>
  </section>

</main>
</body>
</html>
```